I need a graphic for the promotion email for our "8th Annual Brightwater Field Drills Academy" that incorporates our current logo and brand theme. I would like this graphic to funnel potentional attendees to register for a course. My perference would include a cool fire photo from our facility for the background. More information can be found on Kestrelvale.com and also our Facebook.

```html
<!DOCTYPE html>
<html lang="en">
<head>
<meta charset="utf-8">
<title>Brightwater Field Drills Academy</title>
<link rel="stylesheet" href="https://fonts.googleapis.com/css2?family=Montserrat:wght@800;900&family=Oswald:wght@400;500;600&display=swap">
<style>
  :root {
    --ink: #141414;
    --smoke: #3a3a3a;
    --white: #ffffff;
    --red: #e8151b;
    --flame: #f08a12;
    --flame-hot: #ffd24a;
    --gold: #f7c21a;
    --steel: #7c8a94;
    --lime: #c8e43a;
  }
  * { margin: 0; padding: 0; box-sizing: border-box; }
  html, body { width: 1200px; height: 1001px; overflow: hidden; background: var(--ink); }
  .flyer { position: relative; width: 1200px; height: 1001px; overflow: hidden;
    font-family: "Oswald", sans-serif; color: var(--white); }
  .bg-photo { position: absolute; inset: 0;
    background: linear-gradient(100deg, #202020 0%, #2e2e2e 35%, #1d1d1d 60%, #111 100%); }
  .flame-photo { position: absolute; left: 560px; top: 0; width: 460px; height: 1001px;
    background: radial-gradient(ellipse 55% 45% at 50% 40%, var(--flame-hot) 0%, var(--flame) 45%, #c1430a 70%, rgba(30,20,10,0) 100%); }
  .jacket-photo { position: absolute; left: 790px; top: 255px; width: 460px; height: 760px;
    border-radius: 46% 46% 0 0 / 30% 30% 0 0;
    background: linear-gradient(180deg, #2a3038 0%, #1b1f25 60%, #15181d 100%); }
  .tile { position: absolute; right: 0; width: 246px; }
  .tile-hose { top: 0; height: 232px; background: linear-gradient(160deg, #c9d2c8, #8a9288 60%, #b22a2e); }
  .tile-drill { top: 234px; height: 246px; background: linear-gradient(180deg, #d8dde0, #8c8f8c 60%, #4b4f4c); }
  .tile-ladder { top: 482px; height: 312px; background: linear-gradient(180deg, #3c4650, #6d6f55 60%, #2a2f33); }
  .tile-fire { top: 796px; height: 205px; background: linear-gradient(180deg, #e86a16, #3a2a1e); }

  .brand { position: absolute; left: 40px; top: 84px; display: flex; align-items: center; gap: 16px; }
  .brand-mark { width: 60px; height: 60px; border: 4px solid var(--white); border-radius: 50%; }
  .brand-name { font-family: "Montserrat", sans-serif; font-weight: 800; font-size: 34px;
    letter-spacing: 6px; text-transform: uppercase; }

  .title { position: absolute; left: 60px; top: 188px; font-family: "Montserrat", sans-serif;
    font-weight: 900; font-size: 42px; line-height: 53px; letter-spacing: 2px; text-transform: uppercase; }
  .title .accent { color: var(--red); }

  .date { position: absolute; left: 62px; top: 362px; width: 444px; height: 46px; background: var(--red);
    font-family: "Montserrat", sans-serif; font-weight: 900; font-size: 34px; line-height: 46px;
    padding-left: 14px; letter-spacing: 1px; }
  .date sup { font-size: 16px; vertical-align: 14px; line-height: 0; }

  .classes-heading { position: absolute; left: 68px; top: 430px; color: var(--red);
    font-weight: 500; font-size: 32px; text-transform: uppercase; transform: scaleY(1.1); }
  .class-list { position: absolute; left: 66px; top: 482px; list-style: none; }
  .class-item { position: relative; padding-left: 34px; height: 64px; }
  .class-item svg { position: absolute; left: 0; top: 12px; }
  .class-name { font-size: 30px; line-height: 36px; font-weight: 500; display: block; }
  .class-hours { font-size: 15px; line-height: 18px; color: var(--red); display: block; }

  .rule { position: absolute; left: 68px; top: 834px; width: 484px; height: 3px; background: var(--red); }
  .cta { position: absolute; left: 68px; top: 855px; font-size: 29px; line-height: 40px; font-weight: 500; }
  .cta .email { color: var(--gold); border-bottom: 3px solid var(--red); }
</style>
</head>
<body>
<main class="flyer">
  <div class="bg-photo" role="img" aria-label="Dark smoky photo of firefighters training with hoses on a drill field"></div>
  <div class="flame-photo" role="img" aria-label="Large wall of orange flames from a live fire training prop"></div>
  <div class="tile tile-hose" role="img" aria-label="Firefighter operating a red water monitor on a pickup truck"></div>
  <div class="tile tile-drill" role="img" aria-label="Crew in turnout gear fighting a tank fire with hose lines"></div>
  <div class="tile tile-ladder" role="img" aria-label="Steel ladder and platform at the training tower"></div>
  <div class="tile tile-fire" role="img" aria-label="Firefighters advancing on a fire"></div>
  <div class="jacket-photo" role="img" aria-label="Instructor seen from behind in helmet and dark turnout jacket with reflective stripes"></div>

  <div class="brand">
    <span class="brand-mark"></span>
    <span class="brand-name">Kestrelvale</span>
  </div>

  <h1 class="title">8th Annual<br>Brightwater Field<br><span class="accent">Drills Academy</span></h1>

  <div class="date">May 4<sup>th</sup> – 7<sup>th</sup> 2026</div>

  <h2 class="classes-heading">Available Classes:</h2>
  <ul class="class-list">
    <li class="class-item"><svg width="28" height="24" viewBox="0 0 28 24"><path d="M2 13l8 8L26 3" fill="none" stroke="#e8151b" stroke-width="4"/></svg><span class="class-name">Exterior Fire Brigade</span><span class="class-hours">(32 Hours)</span></li>
    <li class="class-item"><svg width="28" height="24" viewBox="0 0 28 24"><path d="M2 13l8 8L26 3" fill="none" stroke="#e8151b" stroke-width="4"/></svg><span class="class-name">Hazardous Materials Technician</span><span class="class-hours">(40 Hours)</span></li>
    <li class="class-item"><svg width="28" height="24" viewBox="0 0 28 24"><path d="M2 13l8 8L26 3" fill="none" stroke="#e8151b" stroke-width="4"/></svg><span class="class-name">Emergency Medical Response</span><span class="class-hours">(40 Hours)</span></li>
    <li class="class-item"><svg width="28" height="24" viewBox="0 0 28 24"><path d="M2 13l8 8L26 3" fill="none" stroke="#e8151b" stroke-width="4"/></svg><span class="class-name">Rope &amp; Confined Space Rescue Technician</span><span class="class-hours">(40 Hours)</span></li>
    <li class="class-item"><svg width="28" height="24" viewBox="0 0 28 24"><path d="M2 13l8 8L26 3" fill="none" stroke="#e8151b" stroke-width="4"/></svg><span class="class-name">Advanced Rope &amp; Confined Space Rescue Technician</span><span class="class-hours">(40 Hours)</span></li>
  </ul>

  <div class="rule"></div>
  <p class="cta">Limited space available! Reach out to<br><span class="email">dana@kestrelvale.com</span> to register! | Location: Harlow Bend, TX</p>
</main>
</body>
</html>
```